Modern Business Card Design Needed for Young Realtor

Information that is going on the card:Marcus Penhall
Broker/Owner
555.013.2967
Marcus@MPenhallHomes.example
www.MPenhallHomes.example

Would also like to include my Instagram Handle somewhere. Probably on the back: the_queencity_realtorMy previous business card is attached, I like that one but would like an updated version and maybe a few design changes

Marcus Penhall
Broker/Owner
555.013.2967
Marcus@MPenhallHomes.example
www.MPenhallHomes.example

• Would also like to include my Instagram Handle somewhere. Probably on the back: the_harborline_agent
• Brantley Osgood or the BO (logo from the previous card.)

```html
<!DOCTYPE html>
<html lang="en">
<head>
<meta charset="utf-8">
<title>MPenhall Homes – Business Card</title>
<link rel="stylesheet" href="https://fonts.googleapis.com/css2?family=Roboto:wght@400;500;700&display=swap">
<style>
  :root {
    --backdrop: #1d1d1e;
    --card-light: #e9e8e7;
    --card-dark: #1e1a1b;
    --brand-red: #a01c26;
    --text-light: #f1f0ef;
    --text-muted: #d9d7d6;
    --logo-dark: #3a3738;
    --photo-top: #6f8a5a;
    --photo-bottom: #5c5c60;
  }
  html, body {
    margin: 0;
    padding: 0;
    width: 1200px;
    height: 896px;
    overflow: hidden;
    background: var(--backdrop);
    font-family: "Roboto", Arial, sans-serif;
  }
  .card {
    position: absolute;
    left: 353px;
    width: 486px;
    height: 278px;
    overflow: hidden;
  }
  .card--front { top: 160px; background: var(--card-light); }
  .card--back { top: 469px; background: var(--card-dark); }

  .front-shape { position: absolute; inset: 0; }

  .wordmark {
    position: absolute;
    margin: 0;
    font-weight: 500;
    letter-spacing: 0.18em;
    white-space: nowrap;
  }
  .card--front .wordmark {
    left: 42px;
    top: 46px;
    font-size: 17px;
    color: var(--brand-red);
  }
  .card--back .wordmark {
    left: 0;
    right: 0;
    top: 138px;
    text-align: center;
    font-size: 26px;
    color: var(--logo-dark);
  }

  .agent {
    position: absolute;
    left: 42px;
    top: 152px;
    color: var(--text-light);
  }
  .agent__name { margin: 0; font-size: 15px; font-weight: 700; line-height: 18px; }
  .agent__title { margin: 0; font-size: 11px; line-height: 14px; color: var(--text-muted); }

  .contact {
    position: absolute;
    left: 42px;
    top: 199px;
    margin: 0;
    padding: 0;
    list-style: none;
    color: var(--text-light);
    font-size: 11px;
    line-height: 14px;
  }
  .contact__item { display: flex; align-items: center; gap: 7px; }
  .contact__icon { width: 8px; height: 8px; flex: none; }

  .portrait {
    position: absolute;
    left: 287px;
    top: 40px;
    width: 153px;
    height: 192px;
    border: 3px solid var(--brand-red);
    border-radius: 6px;
    background: linear-gradient(180deg, var(--photo-top), var(--photo-bottom));
  }

  .social {
    position: absolute;
    left: 0;
    right: 0;
    top: 225px;
    display: flex;
    justify-content: center;
    align-items: center;
    gap: 6px;
    color: var(--text-light);
    font-size: 11px;
  }
  .social__mark { width: 8px; height: 8px; background: var(--text-light); }
</style>
</head>
<body>
  <section class="card card--front">
    <svg class="front-shape" viewBox="0 0 486 278" width="486" height="278" aria-hidden="true">
      <polygon points="0,132 98,93 486,192 486,278 0,278" fill="var(--brand-red)"/>
      <polygon points="0,137 98,98 486,198 486,278 0,278" fill="var(--card-dark)"/>
    </svg>

    <h1 class="wordmark">MPENHALL HOMES</h1>

    <div class="agent">
      <p class="agent__name">Marcus Penhall</p>
      <p class="agent__title">Broker/Owner</p>
    </div>

    <ul class="contact">
      <li class="contact__item">
        <svg class="contact__icon" viewBox="0 0 10 10" aria-hidden="true"><path d="M2 0.5 L3.8 2.6 L2.8 3.6 Q4 6 6.4 7.2 L7.4 6.2 L9.5 8 L8.2 9.5 Q3.5 9 0.5 1.8 Z" fill="var(--text-light)"/></svg>
        <span>555.013.2967</span>
      </li>
      <li class="contact__item">
        <svg class="contact__icon" viewBox="0 0 10 10" aria-hidden="true"><rect x="0.7" y="2" width="8.6" height="6" fill="none" stroke="var(--text-light)" stroke-width="1"/><path d="M0.7 2 L5 5.5 L9.3 2" fill="none" stroke="var(--text-light)" stroke-width="1"/></svg>
        <span>Marcus@MPenhallHomes.example</span>
      </li>
      <li class="contact__item">
        <svg class="contact__icon" viewBox="0 0 10 10" aria-hidden="true"><circle cx="5" cy="5" r="4.3" fill="none" stroke="var(--text-light)" stroke-width="0.9"/><ellipse cx="5" cy="5" rx="1.8" ry="4.3" fill="none" stroke="var(--text-light)" stroke-width="0.8"/><line x1="0.7" y1="5" x2="9.3" y2="5" stroke="var(--text-light)" stroke-width="0.8"/></svg>
        <span>www.MPenhallHomes.example</span>
      </li>
    </ul>

    <div class="portrait" role="img" aria-label="Portrait photo of the agent in a grey blazer, outdoors with greenery behind"></div>
  </section>

  <section class="card card--back">
    <p class="wordmark">MPENHALL HOMES</p>
    <p class="social"><span class="social__mark" aria-hidden="true"></span><span>the_harborline_agent</span></p>
  </section>
</body>
</html>
```